Corporate Web Redesign Project - coded

We would like redesign/refresh of our current site that would allow us to increase the depth of content and create a high quality impression for visitors.

Current site - http://corvanisystems.com/

A previous web redesign project has improved our site but it has not really reached the level we require.

Our customers are global, blue chip, organisations and a professional, corporate style of site is required.

Please note we would prefer a coded website to a just a design. We are happy to provide a zip of our current site if required.
Updates

                                   

Target Market(s)

Global oil and gas producers, KR, Tamberline, Orvadex etc.

Industry/Entity Type

It Professional

Requirements
Must have
• Design should support the level of content we currently have in the existing sitemap - although it should be expandable a site design for a large / complex site would not be appropriate

All current content / pages to be reflected in design

Must be visually appealing

Intuitive and clear navigation that is expandable

Display a high level of professionalism

Use a consistent palette of colours that complements our logo

Clean and organized layout

A way to capture visitor’s information or Call to action (i.e. contact link or form) on every page

Prominent Contact Information
Should not have
• Flash

```html
<!DOCTYPE html>
<html lang="en">
<head>
<meta charset="utf-8">
<title>Corvani Systems</title>
<link href="https://fonts.googleapis.com/css2?family=Roboto:wght@300;400;500;700&display=swap" rel="stylesheet">
<style>
:root{
  --teal:#1f4f5c;
  --teal-btn:#2d6677;
  --olive:#768a52;
  --text:#555d60;
  --muted:#8c9496;
  --band:#dde3e5;
  --footer:#e3e8ea;
  --line:#cdd4d7;
  --white:#fff;
}
*{box-sizing:border-box;margin:0;padding:0}
html,body{width:789px;height:1200px;overflow:hidden}
body{font-family:'Roboto',sans-serif;font-weight:300;color:var(--text);background:var(--white);position:relative}
.abs{position:absolute}
/* header */
.site-header{position:absolute;left:0;top:0;width:789px;height:56px;background:linear-gradient(#fdfdfd,#eeeff0);border-bottom:1px solid #d5d9db}
.brand{position:absolute;left:86px;top:14px;display:flex;align-items:center;gap:6px;font-weight:700;font-size:13px;color:var(--teal);letter-spacing:.3px}
.brand .mark{width:12px;height:12px;border-radius:50%;background:var(--teal)}
.search{position:absolute;left:549px;top:12px;width:155px;height:16px;display:flex}
.search span{flex:1;background:#fff;border:1px solid #e2e4e5;font-size:6px;color:#999;padding:3px 8px}
.search i{width:21px;background:var(--teal);display:flex;align-items:center;justify-content:center}
.main-nav{position:absolute;right:85px;top:37px;font-size:10px;font-weight:400;color:var(--teal);display:flex;gap:10px}
/* hero */
.hero{position:absolute;left:0;top:56px;width:789px;height:314px;background:linear-gradient(90deg,#c9d7e0 0%,#dfe6ea 35%,#c7c9c7 55%,#8d8a85 80%,#6f6a62 100%)}
.hero-copy{position:absolute;left:102px;top:86px}
.hero h1{font-weight:300;font-size:23px;line-height:29px;color:#2b3b40;width:280px}
.hero ul{list-style:none;margin-top:14px}
.hero li{display:flex;align-items:center;gap:9px;font-size:9px;font-weight:400;color:#3a4649;height:21px;padding-left:5px}
.hero li svg{flex:none}
.btn-info{display:inline-block;margin:8px 0 0 5px;background:#f3f4f4;font-size:8px;font-weight:400;color:#444;padding:5px 10px}
.dots{display:flex;gap:3px;margin:10px 0 0 7px}
.dots i{width:9px;height:9px;border-radius:50%;background:#333}
.dots i:first-child{background:var(--olive)}
/* services */
.services{position:absolute;left:0;top:370px;width:789px;height:205px;background:var(--band)}
.service{position:absolute;top:20px;width:160px;text-align:center}
.service svg{display:block;margin:0 auto;height:36px}
.service h3{margin-top:16px;font-size:10px;font-weight:400;color:var(--teal)}
.service p{margin-top:11px;font-size:9px;line-height:15.5px;color:var(--muted)}
.btn-olive{position:absolute;top:158px;left:50%;transform:translateX(-50%);background:var(--olive);color:#fff;font-size:8px;font-weight:400;width:66px;height:23px;line-height:23px;border-radius:6px;text-align:center}
/* content */
.about{position:absolute;left:86px;top:592px;width:408px}
.section-title{font-size:12px;font-weight:400;color:var(--teal);padding-bottom:6px;border-bottom:1px solid var(--line)}
.about p{font-size:9px;line-height:14.5px;margin-top:10px}
.about p+p{margin-top:14px}
.news{position:absolute;left:86px;top:714px;width:408px}
.news .arrows{position:absolute;right:0;top:2px;font-size:14px;color:var(--teal);font-weight:700;letter-spacing:3px}
.news-item{position:relative;padding-left:40px;margin-top:10px}
.news-item .bullet{position:absolute;left:7px;top:0;width:17px;height:17px;border-radius:50%;background:var(--olive);display:flex;align-items:center;justify-content:center}
.news-item h4{font-size:9px;font-weight:400;color:#333}
.news-item p{font-size:9px;line-height:14.5px;margin-top:7px}
.news-item small{display:block;font-size:7.5px;color:#777;margin-top:3px}
.news-item small em{font-style:italic}
.contact-card{position:absolute;left:506px;top:596px;width:198px;height:289px;background:#f4f5f6;border:1px solid #e6e9ea;box-shadow:0 1px 2px rgba(0,0,0,.08)}
.contact-card h2{font-size:12.5px;font-weight:400;color:var(--teal);margin:15px 10px 0;padding-bottom:8px;border-bottom:1px solid var(--line)}
.field{margin:15px 18px 0 13px;height:27px;background:#fff;border:1px solid #e3e6e7;font-size:7px;color:#aab;padding:8px 8px}
.field+.field{margin-top:8px}
.field.msg{height:54px}
.btn-teal{position:absolute;left:65px;top:256px;width:67px;height:23px;line-height:23px;text-align:center;border-radius:6px;background:var(--teal-btn);color:#fff;font-size:8px;font-weight:500}
/* clients */
.rule{position:absolute;left:36px;top:904px;width:717px;height:2px;background:linear-gradient(90deg,transparent,#b8bec1 20%,#8d9598 50%,#b8bec1 80%,transparent)}
.clients{position:absolute;left:86px;top:930px;width:630px;display:flex;justify-content:space-between;align-items:center}
.clients span{font-size:11px;font-weight:500;color:#3d4345;display:flex;align-items:center;gap:4px}
.clients span i{width:9px;height:9px;background:#3d4345}
/* footer */
.site-footer{position:absolute;left:0;top:984px;width:789px;height:152px;background:var(--footer);border-bottom:1px solid #cfd5d8}
.footer-brand{position:absolute;left:86px;top:65px;display:flex;align-items:center;gap:6px;font-size:13px;font-weight:700;color:#4a5457}
.footer-brand i{width:13px;height:13px;border-radius:50%;background:#4a5457}
.footer-col{position:absolute;top:32px;font-size:8.5px;font-weight:400;line-height:15.8px;color:#5b6466}
.footer-col.addr{font-size:8px;line-height:13.8px}
.footer-col h5{font-size:8px;font-weight:400;margin-bottom:14px;letter-spacing:.3px}
.bottom-bar{position:absolute;left:0;top:1137px;width:789px;height:63px;background:var(--footer)}
.copyright{position:absolute;left:86px;top:29px;font-size:8.5px;font-weight:400;color:#555}
.touch{position:absolute;left:355px;top:22px;display:flex;align-items:center;gap:9px;font-size:13px;color:#3b4447}
.badge{position:absolute;left:525px;top:15px;width:180px;height:30px;border-radius:4px;background:#d2d9dc}
</style>
</head>
<body>

<header class="site-header">
  <div class="brand"><span class="mark"></span>CORVANI SYSTEMS</div>
  <div class="search"><span>Search</span><i><svg width="10" height="10" viewBox="0 0 10 10"><circle cx="4" cy="4" r="3" fill="none" stroke="#fff" stroke-width="1.5"/><path d="M6.2 6.2 9 9" stroke="#fff" stroke-width="1.6"/></svg></i></div>
  <nav class="main-nav"><span>Home</span><span>|</span><span>News</span><span>|</span><span>About Us</span><span>|</span><span>Solutions</span><span>|</span><span>Contact Us</span></nav>
</header>

<section class="hero" role="img" aria-label="Photo of a smiling businessman in a grey suit in a bright office, with blurred colleagues talking behind him">
  <div class="hero-copy">
    <h1>Corvani can work with your organization to facilitate:</h1>
    <ul>
      <li><svg width="13" height="13" viewBox="0 0 13 13"><circle cx="6.5" cy="6.5" r="6.5" fill="#3a4346"/><path d="M3.5 6.6 5.7 8.7 9.5 4.5" fill="none" stroke="#fff" stroke-width="1.5"/></svg>Process Mapping and Gap Analysis</li>
      <li><svg width="13" height="13" viewBox="0 0 13 13"><circle cx="6.5" cy="6.5" r="6.5" fill="#3a4346"/><path d="M3.5 6.6 5.7 8.7 9.5 4.5" fill="none" stroke="#fff" stroke-width="1.5"/></svg>Change Management</li>
      <li><svg width="13" height="13" viewBox="0 0 13 13"><circle cx="6.5" cy="6.5" r="6.5" fill="#3a4346"/><path d="M3.5 6.6 5.7 8.7 9.5 4.5" fill="none" stroke="#fff" stroke-width="1.5"/></svg>Project Management</li>
      <li><svg width="13" height="13" viewBox="0 0 13 13"><circle cx="6.5" cy="6.5" r="6.5" fill="#3a4346"/><path d="M3.5 6.6 5.7 8.7 9.5 4.5" fill="none" stroke="#fff" stroke-width="1.5"/></svg>Training</li>
      <li><svg width="13" height="13" viewBox="0 0 13 13"><circle cx="6.5" cy="6.5" r="6.5" fill="#3a4346"/><path d="M3.5 6.6 5.7 8.7 9.5 4.5" fill="none" stroke="#fff" stroke-width="1.5"/></svg>Business and Technical Consulting and Support</li>
    </ul>
    <span class="btn-info">FOR MORE INFO</span>
    <div class="dots"><i></i><i></i><i></i><i></i></div>
  </div>
</section>

<section class="services">
  <div class="service" style="left:80px">
    <svg viewBox="0 0 40 36" width="40"><circle cx="14" cy="22" r="11" fill="none" stroke="#333" stroke-width="2"/><path d="M14 15v7h5" fill="none" stroke="#333" stroke-width="1.8"/><rect x="11" y="8" width="6" height="3" fill="#333"/><rect x="23" y="3" width="14" height="9" rx="1" transform="rotate(-30 30 8)" fill="none" stroke="#333" stroke-width="1.6"/></svg>
    <h3>Time &amp; Cost Estimation</h3>
    <p>RVX delivers a standardized, systematic approach to understanding project risk.</p>
    <span class="btn-olive">Read More</span>
  </div>
  <div class="service" style="left:237px">
    <svg viewBox="0 0 40 36" width="40"><rect x="5" y="8" width="20" height="26" fill="none" stroke="#333" stroke-width="2"/><rect x="9" y="12" width="12" height="5" fill="#333"/><path d="M9 21h12M9 25h12M9 29h12M13 20v11M17 20v11" stroke="#333" stroke-width="1.4"/><rect x="23" y="3" width="14" height="9" rx="1" transform="rotate(-30 30 8)" fill="none" stroke="#333" stroke-width="1.6"/></svg>
    <h3>Materials &amp; Cost Controls</h3>
    <p>CPX has been helping companies optimize materials and cost tracking processes since 1992.</p>
    <span class="btn-olive">Read More</span>
  </div>
  <div class="service" style="left:393px">
    <svg viewBox="0 0 40 36" width="40"><path d="M5 8h14v24H5zM21 8h14v24H21z" fill="none" stroke="#333" stroke-width="2"/><path d="M8 13h8M8 17h8M8 21h8M8 25h8M24 13h8M24 17h8M24 21h8M24 25h8" stroke="#333" stroke-width="1.5"/></svg>
    <h3>Lessons Learned</h3>
    <p>KNX is an advanced lessons learned &amp; knowledge system for use in the energy industry.</p>
    <span class="btn-olive">Read More</span>
  </div>
  <div class="service" style="left:551px">
    <svg viewBox="0 0 40 36" width="40"><circle cx="20" cy="13" r="6.5" fill="#333"/><path d="M10 33c0-8 4-12 10-12s10 4 10 12z" fill="#333"/></svg>
    <h3>Services &amp; Consulting</h3>
    <p>Successful software implementations rely on people and processes to deliver results.</p>
    <span class="btn-olive">Read More</span>
  </div>
</section>

<section class="about">
  <h2 class="section-title">ABOUT US</h2>
  <p>From early phase evaluation through planning, execution and post analysis of wells, we deliver the tools, processes and people required to facilitate major performance improvement and cost savings.</p>
  <p>Our solutions are used in more than 30 countries to support operations ranging from a single well to global deployments with Major Operators.</p>
</section>

<section class="news">
  <h2 class="section-title">LATEST NEWS</h2>
  <span class="arrows">&lsaquo;&rsaquo;</span>
  <article class="news-item">
    <span class="bullet"><svg width="7" height="9" viewBox="0 0 7 9"><path d="M1.5 1 5.5 4.5 1.5 8" fill="none" stroke="#fff" stroke-width="1.6"/></svg></span>
    <h4>RVX Selected by Greymoor</h4>
    <p>Greymoor Energy Ltd has selected RVX as the solution to provide probabilistic time and cost estimates for its drilling operations.</p>
    <small><em>Posted By Corvani Admin,</em> 2013 Aug ,21st &nbsp;GST 22:10</small>
  </article>
  <article class="news-item" style="margin-top:30px">
    <span class="bullet"><svg width="7" height="9" viewBox="0 0 7 9"><path d="M1.5 1 5.5 4.5 1.5 8" fill="none" stroke="#fff" stroke-width="1.6"/></svg></span>
    <h4>CPX Implementation at Enverra</h4>
    <p style="margin-top:4px">Enverra selects CPX to support its materials, logistics &amp; cost management processes.</p>
    <small><em>Posted By Corvani Admin,</em> 2013 Aug ,21st &nbsp;GST 22:10</small>
  </article>
</section>

<aside class="contact-card">
  <h2>Quick Contact Form</h2>
  <div class="field">First name</div>
  <div class="field">Last Name</div>
  <div class="field">E-mail</div>
  <div class="field">Company</div>
  <div class="field msg">Message</div>
  <span class="btn-teal">Read More</span>
</aside>

<div class="rule"></div>
<div class="clients">
  <span><i></i>Orvadex</span>
  <span>Taleno</span>
  <span>Arroyo</span>
  <span>Greymoor</span>
  <span>KR</span>
  <span>Enverra</span>
  <span>Halden</span>
</div>

<footer class="site-footer">
  <div class="footer-brand"><i></i>CORVANI SYSTEMS</div>
  <div class="footer-col" style="left:243px;top:30px">Home<br>News<br>About Us<br>Solutions<br>Contact Us</div>
  <div class="footer-col" style="left:350px;top:30px">Privacy Policy<br>Terms &amp; Conditions<br>Legal Notice</div>
  <div class="footer-col addr" style="left:454px;top:30px"><h5>EUROPE</h5>12 Harlow Row<br>Aberdeen<br>AB11 2QP<br>Phone:+44(0)1224 000123<br>Email: eu@corvanisystems.com</div>
  <div class="footer-col addr" style="left:596px;top:30px"><h5>NORTH AMERICA</h5>1400 Marlin Park Dr<br>Suite 210<br>Houston, TX 77000<br>Phone:(713) 555 0142<br>Email: us@corvanisystems.com</div>
</footer>

<div class="bottom-bar">
  <div class="copyright">Copyright ©2013 &nbsp;Company Name &nbsp;&nbsp;- All rights reserved</div>
  <div class="touch">Get In Touch
    <svg width="12" height="14" viewBox="0 0 12 14"><path d="M2 1l3 3-1.5 2c1 2 2 3 4 4l2-1.5 2.5 3-2 2C5 13 0 7 1 2z" fill="#3b4447"/></svg>
    <svg width="15" height="11" viewBox="0 0 15 11"><rect x="0" y="0" width="15" height="11" fill="#3b4447"/><path d="M0 0l7.5 6L15 0" fill="none" stroke="#e3e8ea" stroke-width="1.2"/></svg>
    <svg width="10" height="14" viewBox="0 0 10 14"><path d="M5 0a5 5 0 0 1 5 5c0 4-5 9-5 9S0 9 0 5a5 5 0 0 1 5-5z" fill="#3b4447"/><circle cx="5" cy="5" r="2" fill="#e3e8ea"/></svg>
  </div>
  <div class="badge" role="img" aria-label="Partner certification badge"></div>
</div>

</body>
</html>
```